Web Design for UK Based Technology Company*

Norvexa is a new entrant in the data marketplace.
It is offering two direct API services to help clients access:
- Company Data
- Location Data
We also offer data services and consulting to help companies to integrate our API services and the data derived from them into their businesses. Our aim is to offer both the technology and services to help businesses use and integrate data better. It is a modern business built to support a modern world.

Target Market(s)

Business Professionals and decision makers

Industry/Entity Type

It Service

Number of Pages Required

5+ page

Font styles to use
Sans Serif

Colors

Designer to choose colors to be used in the design.

Requirements
Must have
• The full suite of PSD designs taking into account the layouts and wireframes supplied with which it will be compared. Focus on the homepage first. It has to have a consistent theme/feel. It has to fit with the logo.
Nice to have
• Simple, clean, a few strong ideas.
Should not have
• Cartoons, overdesign, loud colours.

```html
<!DOCTYPE html>
<html lang="en">
<head>
<meta charset="utf-8">
<title>Norvexa – Richer Data to Drive Your Business</title>
<link rel="stylesheet" href="https://fonts.googleapis.com/css2?family=Open+Sans:wght@400;600;700&display=swap">
<style>
:root{
  --blue:#1a7abf;
  --blue-dark:#145f96;
  --ink:#1f1f1f;
  --text:#444;
  --muted:#777;
  --pink:#f07a98;
  --grad-left:#3f8fc6;
  --grad-right:#f48aa4;
  --contact-bg:#3b3b3d;
  --footer-bg:#2c2c2e;
  --white:#fff;
  --map-green:#4fae8c;
}
*{box-sizing:border-box;margin:0;padding:0}
html,body{width:1200px;height:3689px;overflow:hidden}
body{position:relative;font-family:"Open Sans",Arial,sans-serif;color:var(--text);background:var(--white)}
.abs{position:absolute}
a{color:inherit;text-decoration:none}
.btn{position:absolute;display:flex;align-items:center;justify-content:center;background:var(--blue);color:var(--white);font-size:13px;font-weight:600}
.btn-ghost{background:transparent;border:2px solid var(--white)}

/* header */
.site-header{left:0;top:0;width:1200px;height:110px;background:var(--white)}
.brand{left:123px;top:50px;display:flex;align-items:center;gap:12px;font-size:34px;font-weight:700;color:var(--ink);letter-spacing:1px}
.brand-dot{width:26px;height:26px;background:var(--blue)}
.utility{left:694px;top:23px;font-size:13px;color:var(--blue);display:flex;gap:14px}
.trial{left:964px;top:17px;width:113px;height:33px}
.main-nav{left:510px;top:62px;display:flex;gap:28px;font-size:13px;color:#333}

/* hero */
.hero{left:0;top:110px;width:1200px;height:517px;background:linear-gradient(90deg,#7b8791 0%,#5b6169 45%,#3e3a36 75%,#6d5b4e 100%)}
.hero-title{left:0;top:258px;width:1160px;text-align:center;color:var(--white);font-size:42px;font-weight:700;line-height:52px}
.api-cards{left:123px;top:511px;width:954px;height:197px;background:var(--white);box-shadow:0 6px 18px rgba(0,0,0,.12)}
.api-card{position:absolute;top:0;width:477px;height:197px;text-align:center}
.api-card h3{margin-top:50px;font-size:17px;font-weight:600;color:var(--ink);line-height:24px;text-transform:uppercase}
.api-card .btn{left:50%;transform:translateX(-50%);top:124px;width:154px;height:37px}
.divider{left:470px;top:25px;width:1px;height:146px;background:#ddd}

/* about */
.about-mark{left:123px;top:794px;width:455px;height:305px;display:flex;align-items:center;justify-content:center;gap:18px;font-size:64px;font-weight:700;color:var(--blue)}
.about-mark span.sq{width:40px;height:40px;background:var(--blue)}
.eyebrow{font-size:13px;font-weight:700;color:var(--blue);letter-spacing:1px}
.about-title{left:666px;top:838px;font-size:30px;font-weight:700;color:var(--ink);line-height:42px}
.body-copy{font-size:13px;line-height:22px;color:var(--text)}

/* products */
.photo{position:absolute}
.tag{position:absolute;left:0;top:0;background:var(--blue);color:var(--white);font-size:14px;padding:10px 20px;border-radius:0 0 18px 0}
.prod-title{font-size:18px;font-weight:700;color:var(--ink);text-transform:uppercase}

/* band */
.band{left:0;top:1906px;width:1200px;height:393px}
.band-title{left:125px;top:2064px;font-size:21px;font-weight:700;color:var(--white)}
.band-copy{left:125px;top:2100px;width:870px;font-size:14px;line-height:20px;color:var(--white)}

/* demanding */
.checks{list-style:none}
.checks li{padding-left:22px;position:relative;font-size:13px;line-height:22px}
.checks li::before{content:"»";position:absolute;left:0;color:var(--ink)}

/* contact */
.contact{left:0;top:2852px;width:610px;height:480px;background:var(--contact-bg)}
.contact-line{left:118px;top:2910px;width:1px;height:330px;background:#888}
.call{left:148px;top:2968px;font-size:34px;font-weight:700;color:var(--pink)}
.contact-text{color:#e8e8e8;font-size:15px;line-height:21px}
.newsletter-input{left:148px;top:3147px;width:208px;height:33px;background:var(--white);font-size:12px;color:#999;padding:9px 12px}
.submit{left:366px;top:3147px;width:85px;height:33px;background:var(--pink);color:var(--white);font-size:13px;display:flex;align-items:center;justify-content:center}
.social{position:absolute;top:3237px;width:32px;height:32px;border-radius:50%;background:#6d6d70}
.map{left:612px;top:2852px;width:588px;height:480px;background:linear-gradient(135deg,#eef0e4 0%,#e6ecdc 50%,#dce9d0 100%)}

/* footer */
.footer{left:0;top:3332px;width:1200px;height:357px;background:var(--footer-bg)}
.foot-col{position:absolute;top:3405px;color:#d6d6d6}
.foot-col h4{font-size:15px;font-weight:700;color:var(--white);margin-bottom:14px;text-transform:uppercase}
.foot-col li{list-style:none;font-size:12px;line-height:31px}
.foot-col.wide li{font-size:14px}
.copyright{left:0;top:3620px;width:1200px;text-align:center;font-size:12px;color:#ccc}
</style>
</head>
<body>

<header class="abs site-header">
  <div class="abs brand"><span class="brand-dot"></span>Norvexa</div>
  <div class="abs utility"><a href="#">Contact Us</a><span>|</span><a href="#">0300 000 000</a><span>|</span><a href="#">Login</a></div>
  <a class="btn trial" href="#">Free Trial</a>
  <nav class="abs main-nav" style="left:510px">
    <a href="#">Home</a><a href="#">Company Data</a><a href="#">Company Information</a><a href="#">Services</a><a href="#">Pricing</a><a href="#">Contact Us</a>
  </nav>
</header>

<section class="abs hero" role="img" aria-label="Photo of a man working at a computer screen showing data"></section>
<h1 class="abs hero-title">Richer Data to Drive<br>Your Business</h1>

<div class="abs api-cards">
  <div class="api-card" style="left:0">
    <h3>Comprehensive Compny<br>Incormation</h3>
    <a class="btn" href="#">Company api</a>
  </div>
  <div class="abs divider"></div>
  <div class="api-card" style="left:477px">
    <h3>Bring Mapping Data Into<br>Your Bussness</h3>
    <a class="btn" href="#">Location api</a>
  </div>
</div>

<!-- about -->
<div class="abs about-mark"><span class="sq"></span>Norvexa</div>
<div class="abs eyebrow" style="left:666px;top:794px">ABOUT US</div>
<h2 class="abs about-title">Welcome to<br>Ms. Ledger Wise!</h2>
<p class="abs body-copy" style="left:666px;top:924px;width:430px">My mission is simple- I want to challee you to rethink  way you think about growing, spending and saving money. by redesigning your life around your finances. want you to run your life as if you are the CEO of your own business, your life.</p>
<a class="btn" href="#" style="left:666px;top:1040px;width:128px;height:42px">Read More</a>

<!-- company api -->
<div class="photo" style="left:123px;top:1215px;width:462px;height:297px;background:linear-gradient(135deg,#6f6f70,#2c2c2e 60%,#4a4542)" role="img" aria-label="Photo of hands typing on a laptop">
  <span class="tag">From only $29 pm</span>
</div>
<div class="abs prod-title" style="left:696px;top:1270px">Company API</div>
<p class="abs body-copy" style="left:696px;top:1308px;width:400px">You Supply one or more company numbers-we send back everything via a simple API or CSV file.</p>
<a class="btn" href="#" style="left:696px;top:1384px;width:123px;height:30px;font-size:12px">Find Out More</a>
<a class="btn" href="#" style="left:831px;top:1384px;width:126px;height:30px;font-size:12px">Free Trial</a>

<!-- location api -->
<div class="abs prod-title" style="left:125px;top:1606px">Location API</div>
<p class="abs body-copy" style="left:125px;top:1644px;width:420px">You send us a postcode we send you the location.or  send us the location,we send back the postcode:API or CSV</p>
<a class="btn" href="#" style="left:125px;top:1729px;width:126px;height:30px;font-size:12px">Find Out More</a>
<a class="btn" href="#" style="left:266px;top:1729px;width:123px;height:30px;font-size:12px">Free Trial</a>
<div class="photo" style="left:612px;top:1547px;width:463px;height:297px;background:linear-gradient(135deg,#e4e6e6,#cfe3da 50%,#e4e6e6)" role="img" aria-label="World map with highlighted locations">
  <span class="tag">From only $29 pm</span>
</div>

<!-- gradient band -->
<svg class="abs band" viewBox="0 0 1200 393" preserveAspectRatio="none" aria-hidden="true">
  <defs>
    <linearGradient id="bandFill" x1="0" x2="1" y1="0" y2="0">
      <stop offset="0" stop-color="#3f8fc6"/>
      <stop offset=".5" stop-color="#9a86b0"/>
      <stop offset="1" stop-color="#f48aa4"/>
    </linearGradient>
  </defs>
  <path d="M0 20 C300 -10 500 70 800 40 C1000 20 1100 10 1200 30 L1200 360 C1000 330 850 390 600 390 C350 390 200 330 0 340 Z" fill="url(#bandFill)"/>
</svg>
<h2 class="abs band-title">GO AHEAD : TEST OUR DATA ; OR LET'S TALK IT THROUGH...</h2>
<p class="abs band-copy">Lorem ipsum dolor sit amet, consectetur adipiscing elit, sed do eiusmod tempor incididunt ut labore magna aliqua. Ut enim ad minim veniam, quis nostrud exercitation ullamco laboris nisi ut aliquip ex ea commodo dolore eu fuquis nostrud exercitation ullamco laboris</p>
<a class="btn btn-ghost" href="#" style="left:125px;top:2186px;width:89px;height:35px">Call</a>
<a class="btn btn-ghost" href="#" style="left:236px;top:2186px;width:224px;height:35px">Send an Email</a>

<!-- demanding -->
<div class="photo" style="left:0;top:2380px;width:585px;height:387px;background:linear-gradient(135deg,#4b4a48,#8a8780 50%,#c9c3b8)" role="img" aria-label="Photo of a man reviewing charts with a laptop and phone"></div>
<h2 class="abs prod-title" style="left:671px;top:2402px;width:440px;line-height:26px">Demanding Data Requirements?Look No Further</h2>
<p class="abs body-copy" style="left:671px;top:2462px;width:420px">Lorem ipsum dolor sit amet, consectetur adipiscing elit, sed do eiusmod tempor incididunt ut labore et dolore magna aliqua.</p>
<ul class="abs checks" style="left:671px;top:2522px">
  <li>Excepteur sint occaecat cupidatat non proident.</li>
  <li>Sed ut perspiciatis unde omnis iste natus.</li>
  <li>Nemo enim ipsam voluptatem quia voluptas.</li>
  <li>sed quia consequuntur magni dolores eos qui.</li>
</ul>
<p class="abs body-copy" style="left:671px;top:2620px;width:420px">Lorem ipsum dolor sit amet, consectetur adipiscing elit, incidi call <b style="color:var(--ink)">0000 000 000</b> or .</p>
<a class="btn" href="#" style="left:669px;top:2690px;width:172px;height:42px">Bespoke Services</a>

<!-- contact -->
<section class="abs contact" role="img" aria-label="Dark office photo behind contact details"></section>
<div class="abs contact-line"></div>
<svg class="abs" style="left:102px;top:2975px" width="32" height="32" viewBox="0 0 32 32" aria-hidden="true">
  <circle cx="16" cy="16" r="15" fill="var(--contact-bg)" stroke="#fff" stroke-width="2"/>
  <path d="M11 9c1 0 2 2 2.5 3s-1 2-1 2.5 2.5 4 4 4.5c.5 0 1.5-1.5 2.5-1s3 1.5 3 2.5-1.5 3-3 3C14 23.5 8.5 18 8.5 12 8.5 10.5 10 9 11 9z" fill="#fff"/>
</svg>
<div class="abs call">Call. (000)000.0000</div>
<div class="abs contact-text" style="left:148px;top:3012px">e. contact@norvexa-mail.com</div>
<svg class="abs" style="left:110px;top:3047px" width="16" height="18" viewBox="0 0 16 18" aria-hidden="true"><path d="M8 1a6 6 0 0 1 6 6c0 4-6 10-6 10S2 11 2 7a6 6 0 0 1 6-6z" fill="#fff"/><circle cx="8" cy="7" r="2" fill="var(--contact-bg)"/></svg>
<div class="abs contact-text" style="left:148px;top:3043px;width:330px">Second Floor, 12 Harlow Court Brindle Park<br>Thornbury<br>Reading RG9 4TX</div>
<svg class="abs" style="left:110px;top:3120px" width="16" height="12" viewBox="0 0 16 12" aria-hidden="true"><rect x="0" y="0" width="16" height="12" fill="#fff"/><path d="M0 0l8 6 8-6" stroke="var(--contact-bg)" fill="none" stroke-width="1.5"/></svg>
<div class="abs contact-text" style="left:148px;top:3116px">Newsletter</div>
<div class="abs newsletter-input">Enter Your Email</div>
<a class="abs submit" href="#">Submit</a>
<span class="social" style="left:124px"></span>
<span class="social" style="left:170px;background:var(--pink)"></span>
<span class="social" style="left:212px"></span>
<section class="abs map" role="img" aria-label="Street map showing the office location"></section>

<!-- footer -->
<footer class="abs footer"></footer>
<div class="foot-col" style="left:123px">
  <h4>Company Data</h4>
  <ul><li>Company Information</li><li>Alerts and Notifications</li><li>Contact Information</li><li>Financial Information</li><li>Other Data Services</li></ul>
</div>
<div class="foot-col" style="left:425px">
  <h4>Location Data</h4>
  <ul><li>Postcode Lookup</li><li>Address Lookup</li><li>Base mapping</li><li>Boundaries</li><li>Bespoke Mapping</li></ul>
</div>
<div class="foot-col wide" style="left:693px">
  <h4>Services</h4>
  <ul><li>API/Integrations</li><li>Licensing/IPR</li><li>Complex Location Data</li><li>Digital Transformation</li></ul>
</div>
<div class="foot-col wide" style="left:939px">
  <h4>Norvexa</h4>
  <ul><li>Prcing</li><li>About Us</li><li>Contact Us</li><li>Free Trial</li><li>Login</li></ul>
</div>
<div class="abs copyright">© 2019 Norvexa All Right Reserved &nbsp; | &nbsp; Terms and Conditions &nbsp; | &nbsp; Privacy policy</div>

</body>
</html>
```